Home Equity Lines of Credit
are BACK!!!

* Up to 97.5% on Owner Occupied Properties
* 700 Minimum Scores
* Fund in only 2-3 weeks

Can be used for...
* Education Expense
* Bill Consolidation
* Home Improvement
* Investments

Call today for more information!
(800) 647-2915

Bluecrest Lending Partners, Inc.
NMLS #318660
www.bluecrestlendhub.com

```html
<!DOCTYPE html>
<html lang="en">
<head>
<meta charset="utf-8">
<title>Home Equity Lines of Credit Flyer</title>
<link rel="stylesheet" href="https://fonts.googleapis.com/css2?family=Montserrat:wght@500;600&family=Open+Sans:wght@600;700&display=swap">
<style>
  :root {
    --gold: #a99a35;
    --gold-light: #bfb05a;
    --blue: #2d5395;
    --blue-dark: #254a88;
    --ink-blue: #2f5aa0;
    --white: #ffffff;
    --grey-bar: #b9b9b9;
    --rule: #c9c9c9;
    --photo-light: #f3f3ef;
    --photo-warm: #cdbfa6;
  }
  * { box-sizing: border-box; margin: 0; padding: 0; }
  html, body { width: 1200px; height: 1200px; overflow: hidden; background: var(--white); }
  .flyer {
    position: relative; width: 1200px; height: 1200px; background: var(--white);
    font-family: "Open Sans", Arial, sans-serif; color: var(--ink-blue);
  }
  .hero-photo {
    position: absolute; left: 30px; top: 30px; width: 1140px; height: 665px;
    background: linear-gradient(90deg, var(--white) 0%, var(--photo-light) 30%, #e2dccd 55%, var(--photo-warm) 75%, #d9cfbd 100%);
  }
  .headline-kicker {
    position: absolute; left: 80px; top: 92px;
    font-family: "Montserrat", Arial, sans-serif; font-weight: 600; font-size: 29px; color: var(--blue);
  }
  .headline-main {
    position: absolute; left: 72px; top: 118px;
    font-family: "Montserrat", Arial, sans-serif; font-weight: 500; font-size: 158px; line-height: 1;
    color: var(--gold); letter-spacing: 2px;
  }
  .benefits { position: absolute; left: 80px; top: 320px; width: 350px; list-style: none; }
  .benefits li {
    position: relative; padding: 10px 0 10px 36px; border-bottom: 1px solid var(--rule);
    font-weight: 600; font-size: 22px; line-height: 1.25; color: var(--blue);
  }
  .benefits li:last-child { border-bottom: none; }
  .benefits li strong { font-size: 29px; font-weight: 700; }
  .benefits .tick { position: absolute; left: 0; top: 50%; margin-top: -10px; width: 20px; height: 20px; }
  .uses-band {
    position: absolute; left: 30px; top: 695px; width: 1140px; height: 185px;
    background: linear-gradient(90deg, #3a5f9c 0%, var(--blue) 45%, var(--blue-dark) 100%);
    border-top: 5px solid var(--gold);
    display: flex; align-items: flex-end; padding-bottom: 30px;
  }
  .uses-tab {
    position: absolute; left: 360px; top: -52px; width: 340px; height: 50px;
    background: var(--gold-light); border-radius: 10px 10px 0 0;
    font-family: "Montserrat", Arial, sans-serif; font-weight: 500; font-size: 28px; color: var(--white);
    text-align: center; line-height: 50px; letter-spacing: 1px;
  }
  .use-item {
    flex: 1; display: flex; flex-direction: column; align-items: center; gap: 16px;
    color: var(--white); font-weight: 700; font-size: 21px;
    border-right: 2px dotted rgba(255,255,255,0.55); height: 120px; justify-content: flex-end;
  }
  .use-item:last-child { border-right: none; }
  .use-icon { width: 62px; height: 62px; }
  .brand { position: absolute; left: 70px; top: 925px; width: 340px; text-align: center; }
  .brand-mark { display: flex; align-items: center; justify-content: center; gap: 12px; height: 150px; }
  .brand-dot { width: 26px; height: 26px; border-radius: 50%; background: var(--blue); flex: none; }
  .brand-name { font-weight: 700; font-size: 24px; line-height: 1.2; color: var(--blue); text-align: left; }
  .nmls { margin-top: 22px; font-weight: 600; font-size: 24px; color: var(--blue); }
  .contact { position: absolute; left: 470px; top: 920px; width: 680px; }
  .contact-cta {
    font-family: "Montserrat", Arial, sans-serif; font-weight: 500; font-size: 30px; color: var(--blue);
    padding-bottom: 8px; border-bottom: 1px solid var(--rule); text-align: right;
  }
  .contact-row { display: flex; align-items: center; gap: 26px; margin-top: 18px; }
  .contact-row svg { width: 44px; height: 44px; flex: none; }
  .contact-phone {
    font-family: "Montserrat", Arial, sans-serif; font-weight: 600; font-size: 72px; color: var(--gold); line-height: 1;
  }
  .contact-web { font-weight: 700; font-size: 33px; color: var(--gold); letter-spacing: 4px; }
  .base-bar { position: absolute; left: 30px; bottom: 30px; width: 1140px; height: 16px; background: var(--grey-bar); }
</style>
</head>
<body>
<main class="flyer">
  <div class="hero-photo" role="img" aria-label="Photo of a smiling couple looking at a laptop together in a bright room"></div>

  <p class="headline-kicker">Home Equity Lines of Credit are</p>
  <h1 class="headline-main">BACK!!!</h1>

  <ul class="benefits">
    <li><svg class="tick" viewBox="0 0 20 20"><circle cx="10" cy="10" r="10" fill="#a99a35"/><path d="M5.5 10.5l3 3 6-6.5" fill="none" stroke="#fff" stroke-width="2.2"/></svg>Up to <strong>97.5%</strong> on Owner Occupied Properties</li>
    <li><svg class="tick" viewBox="0 0 20 20"><circle cx="10" cy="10" r="10" fill="#a99a35"/><path d="M5.5 10.5l3 3 6-6.5" fill="none" stroke="#fff" stroke-width="2.2"/></svg><strong>700</strong> Minimum Scores</li>
    <li><svg class="tick" viewBox="0 0 20 20"><circle cx="10" cy="10" r="10" fill="#a99a35"/><path d="M5.5 10.5l3 3 6-6.5" fill="none" stroke="#fff" stroke-width="2.2"/></svg>Fund in only <strong>2-3 weeks</strong></li>
  </ul>

  <section class="uses-band">
    <div class="uses-tab">CAN BE USED FOR</div>
    <div class="use-item">
      <svg class="use-icon" viewBox="0 0 62 62"><circle cx="31" cy="31" r="31" fill="#fff"/><rect x="17" y="34" width="28" height="6" rx="1" fill="#a99a35"/><rect x="19" y="41" width="26" height="6" rx="1" fill="#a99a35"/><path d="M18 24l13-6 13 6-13 6z" fill="#a99a35"/><path d="M24 27v5c4 3 10 3 14 0v-5" fill="#a99a35"/></svg>
      <span>Education Expense</span>
    </div>
    <div class="use-item">
      <svg class="use-icon" viewBox="0 0 62 62"><circle cx="31" cy="31" r="31" fill="#fff"/><path d="M20 15h22v32l-4-3-3 3-4-3-4 3-3-3-4 3z" fill="#a99a35"/><path d="M25 24h12M25 30h12M25 36h8" stroke="#fff" stroke-width="2"/></svg>
      <span>Bill Consolidation</span>
    </div>
    <div class="use-item">
      <svg class="use-icon" viewBox="0 0 62 62"><circle cx="31" cy="31" r="31" fill="#fff"/><path d="M14 32l17-15 17 15h-5v13H19V32z" fill="#a99a35"/><rect x="27" y="35" width="8" height="10" fill="#fff"/></svg>
      <span>Home Improvement</span>
    </div>
    <div class="use-item">
      <svg class="use-icon" viewBox="0 0 62 62"><circle cx="31" cy="31" r="31" fill="#fff"/><path d="M26 16h10l-3 6c8 3 12 10 12 16 0 6-6 9-14 9s-14-3-14-9c0-6 4-13 12-16z" fill="#a99a35"/><text x="31" y="41" text-anchor="middle" font-family="Arial, sans-serif" font-weight="700" font-size="13" fill="#fff">$</text></svg>
      <span>Investments</span>
    </div>
  </section>

  <div class="brand">
    <div class="brand-mark">
      <span class="brand-dot"></span>
      <span class="brand-name">Bluecrest Lending<br>Partners, Inc.</span>
    </div>
    <p class="nmls">NMLS #318660</p>
  </div>

  <section class="contact">
    <p class="contact-cta">CALL TODAY FOR MORE INFORMATION!</p>
    <div class="contact-row">
      <svg viewBox="0 0 44 44"><path d="M10 6l7 1 2 9-5 3c2 5 6 9 11 11l3-5 9 2 1 7c-2 3-5 4-8 4C18 37 7 26 6 14c0-3 1-6 4-8z" fill="#2d5395"/><path d="M28 8a10 10 0 0 1 8 8M27 13a5 5 0 0 1 4 4" fill="none" stroke="#2d5395" stroke-width="2.5"/></svg>
      <span class="contact-phone">(800) 647-2915</span>
    </div>
    <div class="contact-row">
      <svg viewBox="0 0 44 44"><circle cx="22" cy="22" r="18" fill="none" stroke="#2d5395" stroke-width="3"/><ellipse cx="22" cy="22" rx="8" ry="18" fill="none" stroke="#2d5395" stroke-width="2.5"/><path d="M4 22h36M7 13h30M7 31h30" stroke="#2d5395" stroke-width="2.5"/></svg>
      <span class="contact-web">www.bluecrestlendhub.com</span>
    </div>
  </section>

  <div class="base-bar"></div>
</main>
</body>
</html>
```